Cedar Club Food Flyer Postcard

Want a two sided postcard (6x11 quillmark, template attached) designed to be used with TWRK CNPA. The Cedars serves food on Sundays (5-8pm) and Mondays (5-9pm). A menu and other graphics are attached, no need to use all of them. Also want two coupons in the card, $2 dollars off any sandwich, and $2 off any appetizer.

```html
<!DOCTYPE html>
<html lang="en">
<head>
<meta charset="utf-8">
<title>Cedar Club Food Flyer Postcard</title>
<link href="https://fonts.googleapis.com/css2?family=Oswald:wght@400;500;700&family=Montserrat:wght@500;700&family=Dancing+Script:wght@600&family=Arimo:wght@400;700&display=swap" rel="stylesheet">
<style>
  :root{
    --page:#e4e4e4;
    --ink:#111;
    --gold:#e1a52d;
    --gold-deep:#c88d1c;
    --yellow:#ffd93b;
    --red:#d8163a;
    --pink:#dd1158;
    --blue:#1a56a6;
    --navy:#1c2f6e;
    --white:#fff;
    --photo-dark:#1c1512;
  }
  *{box-sizing:border-box;margin:0;padding:0}
  html,body{width:1094px;height:1200px;overflow:hidden;background:var(--page)}
  .card{position:absolute;left:77px;width:940px;height:513px;overflow:hidden;background:var(--white);box-shadow:0 6px 18px rgba(0,0,0,.18)}
  .card--front{top:40px}
  .card--back{top:647px}
  .card svg.bg{position:absolute;inset:0}
  .abs{position:absolute}

  /* front */
  .brand{display:flex;align-items:center;gap:10px;font-family:'Montserrat',sans-serif;font-weight:700;color:var(--navy)}
  .brand__dot{width:22px;height:22px;border-radius:50%;background:var(--white);border:3px solid var(--navy)}
  .brand--front{left:760px;top:150px;font-size:34px}
  .brand--back{left:770px;top:110px;font-size:34px;color:var(--white)}
  .brand--back .brand__dot{border-color:var(--white);background:none}
  .address-front{right:58px;top:303px;text-align:right;font-family:'Montserrat',sans-serif;font-weight:500;font-size:22px;line-height:31px;color:var(--ink)}
  .phone-front{right:55px;top:398px;font-family:'Oswald',sans-serif;font-weight:700;font-size:54px;color:var(--ink);letter-spacing:-1px}

  .coupon{top:368px;height:132px;background:var(--white);border:2px dotted #333;outline:3px solid var(--white);padding:10px 14px 0 24px}
  .coupon--appetizer{left:58px;width:238px}
  .coupon--sandwich{left:318px;width:240px}
  .coupon__amount{font-family:'Oswald',sans-serif;font-weight:700;font-size:68px;line-height:72px;letter-spacing:-2px}
  .coupon__amount .dollars{color:var(--red)}
  .coupon__amount .off{color:#f2b81a}
  .coupon__item{font-family:'Montserrat',sans-serif;font-weight:700;font-size:25px;color:var(--blue);white-space:nowrap}
  .coupon__item .any{font-family:'Dancing Script',cursive;font-weight:600;font-size:24px;color:#222;margin-right:6px}
  .coupon__scissor{position:absolute;font-size:12px;color:#333;font-family:'Arimo',sans-serif}

  /* back */
  .hours{left:42px;top:34px;font-family:'Oswald',sans-serif;color:var(--blue)}
  .hours__title{font-weight:700;font-size:38px;line-height:44px}
  .hours__sub{font-weight:400;font-size:17px;line-height:20px;margin-bottom:6px}
  .hours__bar{background:var(--pink);color:var(--white);font-weight:400;font-size:16px;line-height:27px;padding-left:10px;width:200px;margin-bottom:2px}
  .hours__title--bar{margin-top:6px}
  .partners{left:42px;top:330px;display:flex;align-items:center;gap:34px}
  .partners__name{font-family:'Montserrat',sans-serif;font-weight:700;font-size:20px;color:var(--red)}
  .partners__badge{width:68px;height:56px;background:var(--navy)}
  .address-back{left:42px;top:413px;font-family:'Montserrat',sans-serif;font-weight:500;font-size:14px;line-height:19px;color:var(--ink);white-space:nowrap}
  .phone-back{left:42px;top:452px;font-family:'Oswald',sans-serif;font-weight:700;font-size:38px;line-height:46px;color:var(--blue);letter-spacing:-1px;white-space:nowrap}
  .indicia{left:853px;top:292px;width:78px;height:76px;background:var(--white);border:1.5px solid var(--ink);font-family:'Arimo',sans-serif;font-size:10px;line-height:12.5px;text-align:center;padding-top:6px;color:var(--ink)}
  .indicia b{font-weight:700}
  .mail-panel{left:644px;top:393px;width:296px;height:120px;background:var(--white);border:1.5px solid var(--ink);border-right:none;border-bottom:none;padding:38px 0 0 32px;font-family:'Arimo',sans-serif;font-size:18px;line-height:22px;color:var(--ink)}
</style>
</head>
<body>

<section class="card card--front">
  <svg class="bg" width="940" height="513" viewBox="0 0 940 513">
    <defs>
      <linearGradient id="goldFill" x1="0" y1="0" x2="1" y2="1">
        <stop offset="0" stop-color="#d9981f"/><stop offset="1" stop-color="#e9b23c"/>
      </linearGradient>
      <radialGradient id="sandwichPhoto" cx="0.4" cy="0.45" r="0.6">
        <stop offset="0" stop-color="#b88a5a"/><stop offset="0.55" stop-color="#5a3a22"/><stop offset="1" stop-color="#111"/>
      </radialGradient>
      <radialGradient id="burgerPhoto"><stop offset="0" stop-color="#b9793e"/><stop offset="1" stop-color="#5b3b1f"/></radialGradient>
      <radialGradient id="friesPhoto"><stop offset="0" stop-color="#c79a55"/><stop offset="1" stop-color="#7a5030"/></radialGradient>
    </defs>
    <rect width="940" height="513" fill="url(#goldFill)"/>
    <polygon points="0,0 656,0 474,513 0,513" fill="url(#sandwichPhoto)" role="img" aria-label="Photo of a toasted club sandwich on a plate"/>
    <circle cx="620" cy="108" r="83" fill="var(--white)"/>
    <circle cx="620" cy="108" r="77" fill="url(#burgerPhoto)" role="img" aria-label="Photo of a breaded tenderloin sandwich"/>
    <circle cx="559" cy="262" r="60" fill="var(--white)"/>
    <circle cx="559" cy="262" r="55" fill="url(#friesPhoto)" role="img" aria-label="Photo of chicken strips with fries and dip"/>
  </svg>

  <div class="abs brand brand--front"><span class="brand__dot"></span>Cedars</div>

  <p class="abs address-front">Aerie# 4718<br>218 N Maple Avenue<br>Fairview, NE 68000</p>
  <p class="abs phone-front">402-555-0147</p>

  <div class="abs coupon coupon--appetizer">
    <span class="coupon__scissor" style="left:4px;top:14px">✂</span>
    <div class="coupon__amount"><span class="dollars">$2</span> <span class="off">OFF</span></div>
    <div class="coupon__item"><span class="any">any</span>APPETIZER</div>
  </div>
  <div class="abs coupon coupon--sandwich">
    <span class="coupon__scissor" style="left:4px;top:14px">✂</span>
    <div class="coupon__amount"><span class="dollars">$2</span> <span class="off">OFF</span></div>
    <div class="coupon__item"><span class="any">any</span>SANDWICH</div>
  </div>
</section>

<section class="card card--back">
  <svg class="bg" width="940" height="513" viewBox="0 0 940 513">
    <defs>
      <radialGradient id="meltPhoto" cx="0.55" cy="0.55" r="0.65">
        <stop offset="0" stop-color="#8a5a30"/><stop offset="0.5" stop-color="#4a2c1a"/><stop offset="1" stop-color="#120d0b"/>
      </radialGradient>
      <radialGradient id="bitesPhoto"><stop offset="0" stop-color="#d5a050"/><stop offset="1" stop-color="#a06a2c"/></radialGradient>
      <radialGradient id="nachosPhoto"><stop offset="0" stop-color="#e2b440"/><stop offset="1" stop-color="#7a5424"/></radialGradient>
      <radialGradient id="cheeseburgerPhoto"><stop offset="0" stop-color="#cf8a48"/><stop offset="1" stop-color="#5e3a20"/></radialGradient>
    </defs>
    <rect width="940" height="513" fill="url(#meltPhoto)" role="img" aria-label="Photo of a patty melt on a red checkered paper"/>
    <polygon points="470,0 495,0 312,513 287,513" fill="var(--red)"/>
    <polygon points="0,0 482,0 300,513 0,513" fill="var(--yellow)"/>
    <polygon points="0,0 482,0 300,513 0,513" fill="#f5c52a" opacity="0.35" role="img" aria-label="Faint decorative bird artwork in the yellow panel"/>
    <circle cx="459" cy="77" r="62" fill="var(--white)"/>
    <circle cx="459" cy="77" r="56" fill="url(#bitesPhoto)" role="img" aria-label="Photo of fried cheese bites with dip"/>
    <circle cx="404" cy="243" r="72" fill="var(--white)"/>
    <circle cx="404" cy="243" r="66" fill="url(#nachosPhoto)" role="img" aria-label="Photo of loaded tots with cheese and jalapeños"/>
    <circle cx="356" cy="415" r="90" fill="var(--white)"/>
    <circle cx="356" cy="415" r="84" fill="url(#cheeseburgerPhoto)" role="img" aria-label="Photo of a cheeseburger with tomato and onion"/>
  </svg>

  <div class="abs hours">
    <h2 class="hours__title">GRILL OPEN</h2>
    <p class="hours__sub">DINE - IN OR CARRYOUT</p>
    <p class="hours__bar">Sundays 5 PM - 8 PM</p>
    <p class="hours__bar">Mondays 5 PM - 9 PM</p>
    <h2 class="hours__title hours__title--bar">BAR OPEN</h2>
    <p class="hours__bar">Monday - Friday at 5 PM</p>
    <p class="hours__bar">Saturday at 1 PM</p>
    <p class="hours__bar">Sunday from 2 PM - 8 PM</p>
  </div>

  <div class="abs partners">
    <span class="partners__name">Cedars</span>
    <span class="partners__badge"></span>
  </div>

  <p class="abs address-back">Aerie# 4718, 218 N Maple<br>Avenue Fairview, NE 68000</p>
  <p class="abs phone-back">402-555-0147</p>

  <div class="abs brand brand--back"><span class="brand__dot"></span>Cedars</div>

  <div class="abs indicia">PRSRT STD<br>ECRWSS<br>U.S. POSTAGE<br><b>PAID</b><br>TWRK RETAIL</div>

  <div class="abs mail-panel">Local<br>Postal Customer</div>
</section>

</body>
</html>
```